The Ledgerline Business Card

Business card with QR Code for an accounting and tax business

Target Market(s)

Small Business and Individual Tax

Industry/Entity Type

Bookkeeping, Accounting and Taxes

Contact Information for Business Card

482 WILLOWMERE ST STE 2406 #718342 BOSTON, MA Zip: 02139

Requirements
Must have
• Name and Address

```html
<!DOCTYPE html>
<html lang="en">
<head>
<meta charset="utf-8">
<title>The Ledgerline – Business Card</title>
<link rel="stylesheet" href="https://fonts.googleapis.com/css2?family=Arimo:wght@400;700&display=swap">
<style>
  :root {
    --backdrop: #2a2a2a;
    --card-light: #ffffff;
    --card-dark: #2b2b2b;
    --ink-dark: #1f1f1f;
    --ink-muted: #3a3a3a;
    --ink-light: #ffffff;
    --rule-light: #9a9a9a;
  }
  * { margin: 0; padding: 0; box-sizing: border-box; }
  html, body { width: 1200px; height: 750px; overflow: hidden; }
  body {
    background: var(--backdrop);
    font-family: "Arimo", Arial, sans-serif;
    position: relative;
  }
  .card {
    position: absolute;
    top: 215px;
    width: 520px;
    height: 320px;
    border-radius: 18px;
    box-shadow: 0 10px 30px rgba(0,0,0,0.45);
  }
  /* Front */
  .card-front {
    left: 50px;
    background: var(--card-light);
    color: var(--ink-dark);
    display: flex;
    flex-direction: column;
    align-items: center;
    justify-content: center;
  }
  .brand {
    display: flex;
    align-items: center;
    gap: 16px;
  }
  .brand-dot {
    width: 58px;
    height: 58px;
    border: 5px solid var(--ink-dark);
    border-radius: 50%;
  }
  .brand-name {
    font-weight: 700;
    font-size: 34px;
    letter-spacing: 2px;
    text-transform: uppercase;
  }
  .brand-url {
    margin-top: 48px;
    font-size: 13px;
    letter-spacing: 4px;
    color: var(--ink-muted);
  }
  /* Back */
  .card-back {
    left: 630px;
    background: var(--card-dark);
    color: var(--ink-light);
  }
  .holder {
    position: absolute;
    right: 300px;
    top: 178px;
    text-align: right;
  }
  .holder-name { font-weight: 700; font-size: 24px; }
  .holder-role { font-size: 15px; margin-top: 2px; }
  .divider {
    position: absolute;
    left: 236px;
    top: 62px;
    width: 1px;
    height: 190px;
    background: var(--rule-light);
  }
  .details {
    position: absolute;
    left: 256px;
    top: 70px;
    font-size: 14px;
    line-height: 18px;
  }
  .address { margin-bottom: 22px; }
  .contact-list { list-style: none; }
  .contact-label { font-weight: 700; display: inline-block; width: 22px; }
</style>
</head>
<body>
  <section class="card card-front">
    <div class="brand">
      <span class="brand-dot"></span>
      <span class="brand-name">The Ledgerline</span>
    </div>
    <p class="brand-url">www.THELEDGERLINE.com</p>
  </section>

  <section class="card card-back">
    <div class="holder">
      <p class="holder-name">Owen Hartley</p>
      <p class="holder-role">President</p>
    </div>
    <span class="divider"></span>
    <div class="details">
      <p class="address">482 Willowmere St<br>ste 2406 #718342 Boston<br>MA Zip: 02139</p>
      <ul class="contact-list">
        <li><span class="contact-label">P :</span>(617) 5520-4187</li>
        <li><span class="contact-label">C :</span>(617) 5520-4188</li>
        <li><span class="contact-label">E :</span>name@theledgerline.com</li>
        <li><span class="contact-label">W :</span>www.theledgerline.com</li>
      </ul>
    </div>
  </section>
</body>
</html>
```